Create a new email template des

We are looking for 2 email template designed similar to the attached supplied like Inn Midnight in order to promote of photography business and also our marketing agency.

Both similar in design and branding but with a slight change to the body area.

1. Email is to show images and a little text as attached.
2. Email is to show more text and longer emails with tips and best practices education.

Our website is: www.brookmerestudio.example

The photography site is: http://brookmerestudio.example/hotel-photography/

Target Market(s)

Luxury Hotels

Industry/Entity Type

Business

Requirements
Must have
• Stylish design and as per breif

```html
<!DOCTYPE html>
<html lang="en">
<head>
<meta charset="utf-8">
<title>Brookmere Studio – Hotel Marketing Agency</title>
<link rel="stylesheet" href="https://fonts.googleapis.com/css2?family=Arimo:wght@400;700&family=Cormorant+Garamond:wght@500;600&display=swap">
<style>
:root{
  --frame:#1f1f1f;
  --white:#ffffff;
  --ink:#1c1c22;
  --body:#55565c;
  --muted:#8a8c94;
  --mist:#e5e7ef;
  --navy:#2e3446;
  --footer:#f3f3f3;
  --serif:"Cormorant Garamond", "Times New Roman", serif;
  --sans:Arimo, Arial, sans-serif;
}
*{box-sizing:border-box;margin:0;padding:0}
html,body{width:1200px;height:4528px;overflow:hidden;background:var(--frame)}
body{font-family:var(--sans);color:var(--ink);position:relative}
.email{position:absolute;left:45px;top:0;width:1110px}
section,header,footer{position:relative;width:1110px}
.center{position:absolute;left:0;right:0;text-align:center}

/* header */
.topbar{height:120px;background:var(--frame)}
.brand{position:absolute;left:12px;top:36px;font-family:var(--serif);font-weight:500;font-size:50px;color:var(--white);letter-spacing:1px;text-transform:uppercase}
.nav{position:absolute;right:0;top:54px;display:flex;gap:42px;font-size:22px;color:var(--white);text-transform:uppercase}

/* buttons */
.btn{position:absolute;display:flex;align-items:center;justify-content:center;border:3px solid var(--ink);background:var(--white);font-size:27px;letter-spacing:5px;text-transform:uppercase;color:var(--ink)}

/* hero */
.hero{height:550px}
.hero .photo{position:absolute;inset:0;background:linear-gradient(180deg,#6f7f92 0%,#5f6b6c 35%,#3c4a40 60%,#2f3b45 100%)}
.hero-title{top:265px;font-family:var(--serif);font-weight:500;font-size:56px;letter-spacing:6px;color:var(--white)}
.hero .btn{left:369px;top:385px;width:370px;height:72px;border-color:#2a2a2a}

/* intro */
.intro{height:530px;background:var(--white)}
.section-title{font-weight:700;font-size:44px;letter-spacing:9px;text-transform:uppercase}
.intro .section-title{top:60px}
.tagline{top:132px;font-weight:700;font-size:25px;letter-spacing:4px;text-transform:uppercase}
.intro-copy{position:absolute;left:30px;right:30px;top:210px;text-align:center;font-size:25px;line-height:42px;color:var(--body)}
.intro .btn{left:369px;top:426px;width:370px;height:72px}

/* services */
.services{height:524px;background:var(--mist)}
.feature-icon{position:absolute;left:168px;top:40px}
.feature-title{position:absolute;left:84px;top:158px;font-weight:700;font-size:35px;letter-spacing:2px}
.feature-copy{position:absolute;left:45px;top:220px;width:560px;font-size:32px;line-height:37px;color:#2a2b33}
.services .btn{left:40px;top:375px;width:545px;height:72px}
.service{position:absolute;width:240px;text-align:center;font-size:25px;line-height:30px;color:var(--muted);text-transform:uppercase}
.service svg{display:block;margin:0 auto 10px}

/* gallery */
.gallery{display:grid;grid-template-columns:555px 555px;grid-auto-rows:464px;height:1391px}
.tile{position:relative}
.tile span{position:absolute;left:0;right:0;bottom:60px;text-align:center;font-family:var(--serif);font-weight:500;font-size:33px;letter-spacing:3px;color:var(--white);text-transform:uppercase}
.t1{background:linear-gradient(180deg,#e8a36c 0%,#b0685a 45%,#4b3440 100%)}
.t2{background:linear-gradient(180deg,#1a2c52 0%,#22375a 50%,#1c2a24 100%)}
.t3{background:linear-gradient(180deg,#5a4330 0%,#8a6a48 50%,#3a2a1e 100%)}
.t4{background:linear-gradient(180deg,#7ea9c8 0%,#8e9aa0 45%,#3fb0c8 100%)}
.t5{background:linear-gradient(180deg,#7a5a40 0%,#b48a5c 50%,#6a3a28 100%)}
.t6{background:linear-gradient(180deg,#6a5238 0%,#a68256 50%,#5a3e2a 100%)}

/* audit */
.audit{height:540px;background:var(--navy)}
.audit .section-title{top:50px;color:var(--white);font-size:48px;letter-spacing:6px}
.audit-copy{position:absolute;left:24px;top:170px;width:610px;font-size:27px;line-height:44px;color:var(--white)}
.audit .btn{left:26px;top:402px;width:366px;height:72px}
.screen{position:absolute;left:650px;top:225px;width:421px;height:256px;background:#151515;border-radius:10px;padding:14px}
.screen div{width:100%;height:100%;background:linear-gradient(180deg,#fafafa,#e9e9e9)}
.stand{position:absolute;left:810px;top:481px;width:100px;height:30px;background:linear-gradient(180deg,#c9c9c9,#a9a9a9)}

/* contact */
.contact{height:446px;background:var(--white)}
.contact .section-title{top:38px;font-size:50px;letter-spacing:8px}
.contact-item{position:absolute;width:560px;text-align:center}
.contact-item h3{font-weight:700;font-size:30px;letter-spacing:3px;text-transform:uppercase}
.contact-item p{margin-top:22px;font-size:22px;letter-spacing:2px;color:var(--body);text-transform:uppercase}

/* footer */
.footer{height:375px;background:var(--footer)}
.footer-name{top:62px;font-family:var(--serif);font-weight:600;font-size:46px;letter-spacing:4px;color:var(--ink);text-transform:uppercase}
.social{position:absolute;left:0;right:0;top:188px;display:flex;justify-content:center;gap:22px}
.social i{display:block;width:58px;height:58px;border:2px solid var(--ink);border-radius:50%}
.copyright{top:315px;font-size:20px;letter-spacing:3px;color:var(--body)}
</style>
</head>
<body>
<div class="email">

  <header class="topbar">
    <div class="brand">Brookmere Studio</div>
    <nav class="nav"><span>Home</span><span>About</span><span>Services</span><span>Contact</span></nav>
  </header>

  <section class="hero">
    <div class="photo" role="img" aria-label="Hotel pool terrace with mountains at dusk"></div>
    <h1 class="center hero-title">HOTEL MARKETING AGENCY</h1>
    <div class="btn">Contact Us</div>
  </section>

  <section class="intro">
    <h2 class="center section-title">Hotel Marketing Agency</h2>
    <p class="center tagline">Passoinate &nbsp;-&nbsp; Experienced &nbsp;-&nbsp; Focused</p>
    <p class="intro-copy">Our approach is unique and revolves around our passion to deliver direct business for our clients, driven by our hotel experience and focus on marketing channels that matter the most. Our aim is to help hotels increase web traffic, improve conversion rates and drive direct bookings.</p>
    <div class="btn">Read More</div>
  </section>

  <section class="services">
    <svg class="feature-icon" width="64" height="88" viewBox="0 0 64 88" fill="none" stroke="#2a2b33" stroke-width="3">
      <path d="M18 80h32M22 70h24M26 70l-4-24 18-10-6-18 8-10 10 18v30l-4 14"/>
    </svg>
    <div class="feature-title">SEO FOR HOTELS</div>
    <p class="feature-copy">We create short and long-term hotel SEO strategies that deliver results.</p>
    <div class="btn">View All Services</div>

    <div class="service" style="left:628px;top:48px">
      <svg width="66" height="56" viewBox="0 0 66 56" fill="none" stroke="#9a9ca4" stroke-width="3"><rect x="4" y="4" width="58" height="38" rx="3"/><path d="M24 52h18M33 42v10"/></svg>
      PPC<br>Marketing
    </div>
    <div class="service" style="left:894px;top:40px">
      <svg width="64" height="64" viewBox="0 0 64 64" fill="none" stroke="#9a9ca4" stroke-width="3"><circle cx="32" cy="32" r="28"/><circle cx="32" cy="32" r="18"/><circle cx="32" cy="32" r="8"/></svg>
      Email<br>Marketing
    </div>
    <div class="service" style="left:628px;top:272px">
      <svg width="66" height="56" viewBox="0 0 66 56" fill="none" stroke="#9a9ca4" stroke-width="3"><path d="M6 6h54v34H26l-12 12V40H6z"/><circle cx="22" cy="23" r="2"/><circle cx="33" cy="23" r="2"/><circle cx="44" cy="23" r="2"/></svg>
      Social Media<br>Marketing
    </div>
    <div class="service" style="left:894px;top:272px">
      <svg width="70" height="56" viewBox="0 0 70 56" fill="none" stroke="#9a9ca4" stroke-width="3"><rect x="4" y="12" width="62" height="40" rx="4"/><path d="M24 12l5-8h12l5 8"/><circle cx="35" cy="32" r="12"/></svg>
      Photography
    </div>
  </section>

  <section class="gallery">
    <div class="tile t1" role="img" aria-label="Seafront pavilion at sunset"><span>Saltmere Abu Dhabi</span></div>
    <div class="tile t2" role="img" aria-label="Lit resort terrace by water at night"><span>Lotus Grove Thailand</span></div>
    <div class="tile t3" role="img" aria-label="Hotel dining room with chandelier"><span>Saltmere Abu Dhabi</span></div>
    <div class="tile t4" role="img" aria-label="Pool with sculpted canopies and palm trees"><span>Saltmere Hotels</span></div>
    <div class="tile t5" role="img" aria-label="Hotel bedroom with lake view"><span>Amberlight Palace</span></div>
    <div class="tile t6" role="img" aria-label="Classic hotel suite with draped windows"><span>Hollin House</span></div>
  </section>

  <section class="audit">
    <h2 class="center section-title">Free Hotel SEO Audit</h2>
    <p class="audit-copy">Get in touch with us and we will work on a free comprehensive SEO audit in order to understand the overall health of your hotels digital efforts. We are known to provide one of the best audits in the industry along with a competitor analysis.</p>
    <div class="btn">Contact Us</div>
    <div class="screen"><div role="img" aria-label="Desktop monitor showing the audit report page"></div></div>
    <div class="stand"></div>
  </section>

  <section class="contact">
    <h2 class="center section-title">Contact Us</h2>
    <div class="contact-item" style="left:0;top:150px"><h3>London</h3><p>12 – 14 Alder Row, London EC1 7QP</p></div>
    <div class="contact-item" style="left:550px;top:150px"><h3>Dubai</h3><p>Harbour Point, Marina Walk, Dubai</p></div>
    <div class="contact-item" style="left:0;top:295px"><h3>Email</h3><p>info@brookmerestudio.example</p></div>
    <div class="contact-item" style="left:550px;top:295px"><h3>Website</h3><p>www.brookmerestudio.example</p></div>
  </section>

  <footer class="footer">
    <div class="center footer-name">Brookmere Studio</div>
    <div class="social" aria-label="Social links"><i></i><i></i><i></i><i></i><i></i><i></i></div>
    <p class="center copyright">2017, ALL RIGHTS RESERVED</p>
  </footer>

</div>
</body>
</html>
```